Willow of Meadow Uniform Label Redesign

To refine our current product label designs into one, simple, modern, crisp, general look that can be adapted to all our all Natural Skin Care and Wellness products. I am inspired by the elegant versatility of products like Lumavel Botanic Beauty or Tarn Beauty label schemes. We no longer want labels that indicate scent or ingredients. We have two primary colors that we want to maintain (#096CA3 and #DEE33F), and are willing to entertain subtle additions of others, other than black. Our labels will be printed on white or clear material. We use mainly Cosmo or Boston Round container shapes, plus flat top, smooth, round jars. Maybe a faded watermark highlight the "natural" or "beautiful" side of our products. we need to convey confidence, while remaining simple. We currently use the Advantage font. Maybe Century Gothic may work. Something similar that is easy on the eyes. Maybe vertical main text? We are willing to entertain a lot of ideas. These designs will offer ideas into our eventual Website (www.willowofmeadow-example.com) redesign.

Target Market(s)

Those who are familiar with the power of natural, plant based skin care and wellness products

Industry/Entity Type

Natural Skin Care and Wellness

Font styles to use
Sans Serif
Other font styles liked:
• Century Gothic, Advantage, or similar that is easy on the eyes

Colors
0054AA
0677BA
7BADD7
CADEEF
E8F1F8
59FF00
82FF00
B8FF75
E3FFCB
F4FFEA

Requirements
Must have
• "Clean Lines"; These colors: (#096CA3 and #DEE33F)
Nice to have
• MAYBE vertical main text or a watermark image

```html
<!DOCTYPE html>
<html lang="en">
<head>
<meta charset="utf-8">
<title>Willow of Meadow – Aloe and Shea Hydrating Lotion Label</title>
<link rel="stylesheet" href="https://fonts.googleapis.com/css2?family=Questrial&display=swap">
<style>
  :root {
    --brand-blue: #096ca3;
    --brand-blue-light: #3a93cc;
    --brand-lime: #dee33f;
    --brand-lime-deep: #cdd62a;
    --ink: #1c1a0e;
    --olive: #7d7c22;
    --olive-dark: #5b5a1a;
    --white: #ffffff;
  }
  html, body {
    margin: 0;
    padding: 0;
    width: 1200px;
    height: 3076px;
    overflow: hidden;
    background: var(--white);
  }
  .label {
    position: relative;
    width: 1200px;
    height: 3076px;
    font-family: "Questrial", "Century Gothic", sans-serif;
    background: linear-gradient(90deg, var(--brand-lime-deep) 0%, var(--brand-lime) 30%, var(--brand-lime) 70%, var(--brand-lime-deep) 100%);
    overflow: hidden;
  }
  .brand-band {
    position: absolute;
    left: 0;
    top: 0;
    width: 1200px;
    height: 500px;
    background: linear-gradient(90deg, var(--brand-blue) 0%, var(--brand-blue-light) 55%, var(--brand-blue) 100%);
    border-bottom: 10px solid var(--white);
    color: var(--white);
    text-align: center;
  }
  .brand-name {
    position: absolute;
    left: 0;
    right: 0;
    top: 150px;
    margin: 0;
    display: flex;
    justify-content: center;
    align-items: center;
    gap: 30px;
    font-size: 84px;
    font-weight: 400;
    letter-spacing: 8px;
    text-transform: uppercase;
    line-height: 1;
  }
  .brand-dot {
    width: 34px;
    height: 34px;
    border-radius: 50%;
    background: var(--white);
    flex: none;
  }
  .brand-tagline {
    position: absolute;
    left: 0;
    right: 0;
    top: 300px;
    margin: 0;
    font-size: 54px;
    letter-spacing: 2px;
    line-height: 1;
  }
  .product {
    position: absolute;
    left: 0;
    right: 0;
    top: 640px;
    text-align: center;
    color: var(--ink);
  }
  .product-title {
    margin: 0;
    font-weight: 400;
    line-height: 1;
  }
  .product-title .word {
    display: block;
    font-size: 250px;
    letter-spacing: 4px;
  }
  .product-title .joiner {
    display: block;
    font-size: 72px;
    margin: 14px 0 6px;
  }
  .product-type {
    margin: 150px 0 0;
    font-size: 100px;
    line-height: 1;
  }
  .divider {
    position: absolute;
    left: 398px;
    top: 1602px;
    width: 405px;
    height: 26px;
    background: var(--olive);
  }
  .botanical-art {
    position: absolute;
    left: 150px;
    top: 1700px;
    width: 960px;
    height: 1040px;
    background: radial-gradient(ellipse 50% 50% at 50% 55%, rgba(91, 90, 26, 0.85) 0%, rgba(91, 90, 26, 0.5) 55%, rgba(91, 90, 26, 0) 100%);
  }
  .volume {
    position: absolute;
    right: 100px;
    top: 2960px;
    margin: 0;
    font-size: 68px;
    color: var(--ink);
    line-height: 1;
    transform: rotate(-4deg);
    transform-origin: right center;
  }
</style>
</head>
<body>
  <main class="label">
    <header class="brand-band">
      <h1 class="brand-name"><span class="brand-dot"></span>Willow of Meadow</h1>
      <p class="brand-tagline">Pure. Gentle. Plant Made.</p>
    </header>

    <section class="product">
      <h2 class="product-title">
        <span class="word">ALOE</span>
        <span class="joiner">and</span>
        <span class="word">SHEA</span>
      </h2>
      <p class="product-type">Hydrating Lotion</p>
    </section>

    <div class="divider"></div>

    <div class="botanical-art" role="img" aria-label="Olive-toned silhouette illustration of an aloe vera plant with spiky leaves"></div>

    <p class="volume">8 fl. oz (238 ml)</p>
  </main>
</body>
</html>
```